Facebook Ads for Leading Telemedicine Provider

Need a variation of this advertisement.

Would like to leave everything the same with white as the dominant color but test the pink circle with a different design style

Target Market(s)

Male / Female from 18-65

Industry/Entity Type

Health

Requirements
Must have
• Use the image attached and test a different background

```html
<!DOCTYPE html>
<html lang="en">
<head>
<meta charset="utf-8">
<title>Wellora – Free Covid Testing at Home</title>
<link rel="stylesheet" href="https://fonts.googleapis.com/css2?family=Lato:wght@400;700&family=Montserrat:ital,wght@0,600;0,700;1,600&display=swap">
<style>
  :root {
    --plum: #8d7a93;
    --rose: #b4868a;
    --coral: #e8976a;
    --sand: #f4e2b6;
    --white: #ffffff;
    --ink: #1c1c1c;
    --slate: #5b5f7a;
    --mustard: #d3a23a;
    --virus: #5fbf8a;
  }
  html, body {
    margin: 0;
    padding: 0;
    width: 1200px;
    height: 1200px;
    overflow: hidden;
    background: var(--white);
  }
  .ad {
    position: relative;
    width: 1200px;
    height: 1200px;
    overflow: hidden;
    background: var(--white);
    font-family: "Montserrat", sans-serif;
  }
  /* New background style: a curved colour panel on a white canvas */
  .hero-panel {
    position: absolute;
    left: 0;
    top: 0;
    width: 1200px;
    height: 620px;
    border-bottom-right-radius: 560px 540px;
    background: linear-gradient(135deg, var(--plum) 0%, var(--rose) 45%, var(--coral) 100%);
  }
  .accent-ring {
    position: absolute;
    border-radius: 50%;
    border: 3px solid var(--sand);
  }
  .accent-ring-top {
    left: 900px;
    top: -160px;
    width: 420px;
    height: 420px;
    border-color: rgba(244,226,182,0.7);
  }
  .accent-dot-left {
    position: absolute;
    left: -90px;
    top: 930px;
    width: 180px;
    height: 180px;
    border-radius: 50%;
    background: var(--sand);
    opacity: 0.6;
  }
  .brand-name {
    position: absolute;
    left: 114px;
    top: 104px;
    margin: 0;
    font-weight: 700;
    font-size: 60px;
    line-height: 1;
    color: var(--white);
    letter-spacing: -1px;
  }
  .headline {
    position: absolute;
    margin: 0;
    color: var(--white);
    line-height: 1;
    font-weight: 600;
  }
  .headline-free {
    left: 110px;
    top: 236px;
    font-size: 100px;
    font-weight: 700;
    letter-spacing: -1px;
  }
  .headline-service {
    left: 208px;
    top: 344px;
    font-size: 96px;
    font-style: italic;
    letter-spacing: 0.5px;
  }
  .headline-place {
    left: 614px;
    top: 446px;
    font-size: 58px;
  }
  .headline-rule {
    position: absolute;
    left: 0;
    top: 484px;
    width: 596px;
    height: 3px;
    background: var(--white);
  }
  .no-virus-icon {
    position: absolute;
    left: 964px;
    top: 352px;
    width: 140px;
    height: 140px;
  }
  .scene-illustration {
    position: absolute;
    left: 516px;
    top: 516px;
    width: 674px;
    height: 592px;
    border-radius: 14px;
    background: linear-gradient(160deg, #f6e3ad 0%, var(--mustard) 55%, var(--slate) 100%);
    opacity: 0.85;
  }
  .book-button {
    position: absolute;
    left: 103px;
    top: 792px;
    width: 355px;
    height: 84px;
    border-radius: 8px;
    background: linear-gradient(90deg, var(--plum) 0%, #b08690 45%, var(--coral) 80%, #f5d2aa 100%);
    box-shadow: 0 6px 12px rgba(0,0,0,0.28), inset 0 0 0 3px rgba(255,255,255,0.6);
    display: flex;
    align-items: center;
    justify-content: center;
    font-family: "Lato", sans-serif;
    font-weight: 400;
    font-size: 40px;
    color: var(--white);
    letter-spacing: 0.5px;
    text-decoration: none;
  }
  .web-address {
    position: absolute;
    left: 103px;
    top: 1084px;
    margin: 0;
    font-family: "Lato", sans-serif;
    font-weight: 700;
    font-size: 24px;
    color: var(--ink);
  }
  .footer-rule {
    position: absolute;
    left: 103px;
    top: 1127px;
    width: 1097px;
    height: 3px;
    background: linear-gradient(90deg, #f6dcae 0%, var(--coral) 50%, var(--plum) 100%);
  }
</style>
</head>
<body>
  <main class="ad">
    <div class="hero-panel"></div>
    <div class="accent-ring accent-ring-top"></div>
    <div class="accent-dot-left"></div>

    <p class="brand-name">Wellora</p>

    <h1 class="headline headline-free">FREE</h1>
    <h2 class="headline headline-service">Covid Testing</h2>
    <div class="headline-rule"></div>
    <h2 class="headline headline-place">at Home</h2>

    <svg class="no-virus-icon" viewBox="0 0 140 140" aria-hidden="true">
      <g stroke="var(--virus)" stroke-width="4" stroke-linecap="round">
        <line x1="70" y1="34" x2="70" y2="106"/>
        <line x1="34" y1="70" x2="106" y2="70"/>
        <line x1="45" y1="45" x2="95" y2="95"/>
        <line x1="95" y1="45" x2="45" y2="95"/>
      </g>
      <circle cx="70" cy="70" r="24" fill="var(--virus)"/>
      <circle cx="70" cy="70" r="62" fill="none" stroke="var(--slate)" stroke-width="10"/>
      <line x1="26" y1="26" x2="114" y2="114" stroke="var(--slate)" stroke-width="10"/>
    </svg>

    <div class="scene-illustration" role="img" aria-label="Illustration of a woman opening her front door to a masked health worker holding a clipboard, with a welcome mat, potted plant and a checkmark badge"></div>

    <a class="book-button" href="#">BOOK NOW</a>

    <p class="web-address">https://wellora.org/covid-testing</p>
    <div class="footer-rule"></div>
  </main>
</body>
</html>
```